New Corporate Business Card - Velmorabelle

What we need:
We need a new corporate business card.
We want a new template that we can change by ourself.
We want business card modern and minimalist but that looks professional.
We will print it in 300 gr soft-touch.
Why not a white side with the logo and a red/grey side with the content?
Why not a grey side and a red side like our logo?
I am sure that you have better idea than ours that's the reason we come here.

Who we are:
We are a private label company in cosmetics based in Switzerland. We work in BtoB. We make skin care products for other brands.

Target Market(s)

B to B - Worldwide - any gender

Industry/Entity Type

Cosmetics

Contact Information for Business Card

Side 1:
Logo
Your Swiss Private Label Manufacturer or www.velmorabelle.ch

Side 2:
Name and surname (Example: Lucien Marchetaz)
Job Description (General Manager)
Telephone (+41 32 918 64 00)
Direct (+41 32 918 64 64)
Email (lucien.marchetaz@velmorabelle.ch)
Chemin des Prés-Fleuris 14, 2000 Neuchâtel, Switzerland
www.velmorabelle.ch

Font styles to use
Serif
Sans Serif

Requirements
Must have
• You can use 4 colors: white, red, grey and/or black .
Should not have
• Too much colors, too much things. We want it simple!

```html
<!DOCTYPE html>
<html lang="en">
<head>
<meta charset="utf-8">
<title>Velmorabelle – Business Card</title>
<link rel="stylesheet" href="https://fonts.googleapis.com/css2?family=Jost:wght@400;500;600&display=swap">
<style>
  :root {
    --backdrop: #4a4b4e;
    --card-white: #e6e6e6;
    --brand-red: #e82e26;
    --brand-grey: #a7a8ab;
    --ink-white: #ffffff;
    --ink-grey: #9c9da0;
  }
  * { margin: 0; padding: 0; box-sizing: border-box; }
  html, body { width: 1200px; height: 1000px; overflow: hidden; }
  body {
    background: var(--backdrop);
    font-family: "Jost", "Helvetica Neue", Arial, sans-serif;
    position: relative;
  }
  .card {
    position: absolute;
    left: 260px;
    width: 680px;
    height: 440px;
    border-radius: 26px;
  }
  .card--front { top: 40px; background: var(--card-white); }
  .card--back { top: 520px; background: var(--brand-red); color: var(--ink-white); }

  .wordmark {
    display: flex;
    align-items: center;
    gap: 14px;
    font-weight: 500;
    letter-spacing: 0.08em;
  }
  .wordmark__square { width: 22px; height: 22px; }
  .card--front .wordmark {
    position: absolute;
    left: 0; right: 0; top: 0; bottom: 0;
    justify-content: center;
    font-size: 46px;
    color: var(--brand-red);
  }
  .card--front .wordmark__square { background: var(--brand-grey); }
  .card--back .wordmark {
    position: absolute;
    left: 40px; top: 190px;
    font-size: 30px;
    color: var(--ink-white);
  }
  .card--back .wordmark__square { background: var(--ink-white); width: 18px; height: 18px; }

  .divider {
    position: absolute;
    left: 330px;
    width: 3px;
    background: var(--ink-white);
  }
  .divider--name { top: 112px; height: 46px; }
  .divider--details { top: 172px; height: 156px; background: var(--brand-grey); }

  .contact { position: absolute; left: 352px; top: 112px; }
  .contact__name {
    font-weight: 600;
    font-size: 23px;
    letter-spacing: 0.02em;
    text-transform: uppercase;
    line-height: 1.1;
  }
  .contact__role { font-size: 16px; margin-top: 2px; }
  .contact__details {
    list-style: none;
    margin-top: 20px;
    font-size: 15.5px;
    line-height: 1.4;
  }
  .contact__details li { display: flex; align-items: center; gap: 7px; }
  .contact__details svg { width: 13px; height: 13px; flex: none; }
</style>
</head>
<body>
  <section class="card card--front" aria-label="Card front">
    <div class="wordmark"><span class="wordmark__square"></span>Velmorabelle</div>
  </section>

  <section class="card card--back" aria-label="Card back">
    <div class="wordmark"><span class="wordmark__square"></span>Velmorabelle</div>

    <span class="divider divider--name"></span>
    <span class="divider divider--details"></span>

    <div class="contact">
      <h1 class="contact__name">Lucien Marchetaz</h1>
      <p class="contact__role">General Manager</p>
      <ul class="contact__details">
        <li>Chemin des Prés-Fleuris 14,</li>
        <li>2000 Neuchâtel, Switzerland</li>
        <li>Tel: +41 32 918 64 00</li>
        <li>Direct: +41 32 918 64 64</li>
        <li>
          <svg viewBox="0 0 14 14" aria-hidden="true"><rect x="1" y="3" width="12" height="8" fill="none" stroke="#fff" stroke-width="1.4"/><path d="M1 3 L7 8 L13 3" fill="none" stroke="#fff" stroke-width="1.4"/></svg>
          lucien.marchetaz@velmorabelle.ch
        </li>
        <li>
          <svg viewBox="0 0 14 14" aria-hidden="true"><circle cx="7" cy="7" r="5.8" fill="none" stroke="#fff" stroke-width="1.3"/><ellipse cx="7" cy="7" rx="2.6" ry="5.8" fill="none" stroke="#fff" stroke-width="1.1"/><path d="M1.2 7 H12.8" stroke="#fff" stroke-width="1.1"/></svg>
          www.velmorabelle.ch
        </li>
      </ul>
    </div>
  </section>
</body>
</html>
```